New design for www.TrimTable.com

On TrimTable you can find & book your hairdresser. TrimTable is the biggest platform in the Netherlands.

- The design should be a responcive design
- Should be able to go global, should fit in perfectly between all the big booking platforms like roomquay, zipvan etc,
- Should have te result of more bookings. :)
- We are ‘only’ asking a beautiful design, not a technical solution.
- We need a homepage (https://trimtable.com/), search resultpage ((https://trimtable.com/kapper/amsterdam/#), salonpage (https://trimtable.com/kapper/vorden/sol-mira-hair/), about us page (https://trimtable.com/aboutus/), for the hairdresser info page (https://trimtable.com/kapper/), login/register page (https://trimtable.com/account/signin/).

- On the page of the hairdresser there is a dynamic part. The part where you create your appointment. Please take a look at this part too after you choose your treatment (behandeling), employee (medewerker), Date (datum) and time (tijd). The part that you see after this, is the part where you fill in your data as a consumer.

I've added more logo's but mostly we use the green color.

A few of our competitors: www.glowpick.com, www.kestoly.com

Target Market(s)

All consumers

Industry/Entity Type

Hair And Beauty

Number of Pages Required

5+ page

Font styles to use
Sans Serif

Colors
abd036
c3c3c3
757575

Requirements
Must have
• Responsive
• We did an A/B test with the homepage. It turns out that option B works better then option A (take a look at the uploaded pictures). So what we need on the homepage: The USP's with the green checkboxes, The search button needs to by dynamic (changes for example from light green to dark green so you can see you can click it) The call to action sentence Zoek & Vind je kapsalon, the searchfield and searchbutton should be seperated.
Nice to have
• The style that we like is the flat design style. The website should be simple, clean and it should feel a bit like a luxury thing. Because an appointment with the hairdresser can be a real treat and luxury moment for yourself.
• The luxury feeling and flat design that is in the www.zipvan.com website is really nice for example. But then it has to be a bit more light and not so black and dark.

```html
<!DOCTYPE html>
<html lang="en">
<head>
<meta charset="utf-8">
<title>TrimTable – Find &amp; book your hairdresser</title>
<link href="https://fonts.googleapis.com/css2?family=Roboto:wght@300;400;500;700&family=Roboto+Condensed:wght@400;700&display=swap" rel="stylesheet">
<style>
:root{
  --green:#abd036;
  --green-dark:#93b82a;
  --orange:#f47b20;
  --ink:#2e2e2e;
  --grey:#757575;
  --grey-light:#c3c3c3;
  --paper:#ffffff;
  --soft:#f4f4f4;
  --night:#232323;
  --night-2:#1b1b1b;
}
*{box-sizing:border-box;margin:0;padding:0}
html,body{width:1200px;height:2792px;overflow:hidden}
body{position:relative;background:var(--paper);font-family:"Roboto",sans-serif;color:var(--ink)}
.cond{font-family:"Roboto Condensed","Roboto",sans-serif}
section,header,footer{position:absolute;left:0;width:1200px}

/* hero */
.hero{top:0;height:400px;overflow:hidden}
.hero-photo{position:absolute;inset:0;background:linear-gradient(100deg,#1d2224 0%,#3a3f3f 45%,#5a5852 70%,#2a2b2a 100%)}
.hero-shade{position:absolute;inset:0;background:rgba(0,0,0,.35)}
.brand{position:absolute;left:32px;top:26px;display:flex;align-items:center;gap:10px;color:#fff;font-weight:700;font-size:26px}
.brand-dot{width:30px;height:30px;border-radius:50%;background:#fff}
.nav-btns{position:absolute;right:34px;top:40px;display:flex;gap:12px}
.nav-btn{border:1px solid rgba(255,255,255,.8);color:#fff;font-size:13px;padding:6px 12px;letter-spacing:.5px}
.hero-title{position:absolute;top:112px;width:100%;text-align:center;color:#fff;font-weight:700;font-size:64px;letter-spacing:1px}
.hero-sub{position:absolute;top:196px;width:100%;text-align:center;color:#fff;font-size:15px;letter-spacing:.5px}
.search-row{position:absolute;display:flex;height:40px}
.search-row .field{background:#fff;color:var(--grey);font-size:13px;display:flex;align-items:center;padding:0 16px}
.search-row .select{border-left:1px solid #ddd;justify-content:space-between}
.search-row .go{background:var(--orange);color:#fff;font-size:13px;display:flex;align-items:center;justify-content:center;font-weight:500}
.row-one{left:340px;top:256px}
.row-two{left:480px;top:322px}
.slide-arrow{position:absolute;top:180px}

/* intro */
.intro{top:400px;height:440px;background:var(--paper)}
.intro h2{position:absolute;top:50px;width:100%;text-align:center;font-weight:400;font-size:54px;color:var(--grey)}
.intro .last{position:absolute;top:116px;width:100%;text-align:center;color:var(--green);font-size:17px}
.laptop{position:absolute;left:200px;top:170px;width:290px;height:210px}
.features{position:absolute;left:580px;top:200px;display:grid;grid-template-columns:300px 300px;row-gap:34px}
.feature{display:flex;gap:16px}
.feature-icon{width:42px;height:42px;background:#3f4548;flex:none;display:flex;align-items:center;justify-content:center}
.feature h3{font-size:16px;font-weight:500;color:var(--ink);margin-bottom:4px}
.feature p{font-size:12px;line-height:16px;color:var(--grey)}

/* app band */
.app{top:840px;height:370px;overflow:hidden}
.app-photo{position:absolute;inset:0;background:linear-gradient(90deg,#8fb32a 0%,#abd036 50%,#9ec22f 100%)}
.notch-top{position:absolute;left:560px;top:0}
.phones{position:absolute;left:200px;top:40px;width:260px;height:310px}
.app-copy{position:absolute;left:630px;top:100px;color:#fff}
.app-copy h2{font-size:46px;font-weight:700;line-height:48px}
.app-copy .lead{font-size:20px;font-weight:300;margin-top:4px}
.app-copy .small{font-size:13px;line-height:18px;margin-top:12px;width:380px}
.badges{display:flex;gap:14px;margin-top:18px}
.badge{width:140px;height:40px;background:#111;border-radius:6px}
.app-btn{margin-top:20px;display:inline-block;border:1px solid #fff;padding:9px 20px;font-size:12px;letter-spacing:.5px}

/* steps */
.steps{top:1210px;height:490px;background:var(--paper)}
.notch-bottom{position:absolute;left:560px;top:-1px}
.steps h2{position:absolute;top:80px;width:100%;text-align:center;font-size:40px;font-weight:400;color:var(--ink)}
.steps-line{position:absolute;left:260px;top:245px}
.step{position:absolute;top:170px;width:260px;text-align:center}
.step h3{font-size:15px;font-weight:500;margin-top:20px;line-height:20px}
.step p{font-size:12px;line-height:16px;color:var(--grey);margin-top:6px}

/* newsletter */
.news{top:1700px;height:420px;overflow:hidden}
.news-photo{position:absolute;inset:0;background:linear-gradient(135deg,#2d2d2d 0%,#474747 40%,#1f1f1f 100%)}
.news-shade{position:absolute;inset:0;background:rgba(0,0,0,.45)}
.news h2{position:absolute;top:134px;width:100%;text-align:center;color:#fff;font-weight:700;font-size:44px}
.news .lead{position:absolute;top:198px;width:100%;text-align:center;color:#fff;font-size:16px;line-height:22px}
.news-form{position:absolute;left:240px;top:290px;display:flex;height:56px}
.news-input{width:480px;background:rgba(0,0,0,.6);border:1px solid #555;color:#999;font-size:14px;display:flex;align-items:center;padding-left:60px;position:relative}
.news-input svg{position:absolute;left:20px;top:18px}
.news-btn{width:170px;background:var(--green);color:#fff;font-weight:700;font-size:16px;display:flex;align-items:center;justify-content:center}

/* footer */
.footer{top:2120px;height:630px;background:var(--night)}
.foot-logo{position:absolute;left:100px;top:70px;display:flex;flex-direction:column;align-items:center;gap:12px}
.foot-logo .mark{width:100px;height:100px;border-radius:50%;background:var(--green)}
.foot-logo span{color:var(--green);font-weight:700;font-size:22px}
.foot-col{position:absolute;top:72px;color:#bbb}
.foot-col h4{color:#fff;font-size:15px;font-weight:700;margin-bottom:14px;letter-spacing:.5px}
.foot-col li{list-style:none;font-size:12px;line-height:24px}
.social li{display:flex;align-items:center;gap:10px;line-height:32px}
.social i{width:22px;height:22px;border-radius:50%;border:1px solid #888;display:inline-block}
.copyright{top:2750px;height:42px;background:var(--green);color:#fff;font-size:12px;display:flex;align-items:center;justify-content:center}
.page-no{position:absolute;right:20px;top:2700px;color:#888;font-size:12px}
</style>
</head>
<body>

<header class="hero">
  <div class="hero-photo" role="img" aria-label="Photo of a man smiling while booking on a laptop in a salon"></div>
  <div class="hero-shade"></div>
  <div class="brand"><span class="brand-dot"></span>TrimTable</div>
  <nav class="nav-btns"><span class="nav-btn">LOG IN</span><span class="nav-btn">REGISTER</span></nav>
  <svg class="slide-arrow" style="left:18px" width="20" height="40" viewBox="0 0 20 40"><path d="M16 4 L4 20 L16 36" fill="none" stroke="#fff" stroke-width="2"/></svg>
  <svg class="slide-arrow" style="right:18px" width="20" height="40" viewBox="0 0 20 40"><path d="M4 4 L16 20 L4 36" fill="none" stroke="#fff" stroke-width="2"/></svg>
  <h1 class="hero-title cond">TRIMTABLE</h1>
  <p class="hero-sub cond">THE GREATEST HAIRDRESSER BOOKING SITE IN THE NETHERLANDS WITH 5K HAIRDRESSERS</p>
  <div class="search-row row-one">
    <div class="field" style="width:300px">Search by place or postcode</div>
    <div class="field select" style="width:160px">All treatments <span>▾</span></div>
    <div class="go" style="width:60px">SEARCH</div>
  </div>
  <div class="search-row row-two">
    <div class="field" style="width:240px">Search by salon name</div>
    <div class="go" style="width:60px">FIND</div>
  </div>
</header>

<section class="intro">
  <h2 class="cond">TrimTable</h2>
  <p class="last">Last appointment on October 15, 2015 at 17:00</p>
  <div class="laptop" role="img" aria-label="Illustration of a laptop showing the TrimTable site in green"></div>
  <svg class="laptop" viewBox="0 0 290 210" aria-hidden="true">
    <rect x="40" y="10" width="210" height="140" rx="6" fill="#3a3a3a"/>
    <rect x="50" y="20" width="190" height="120" fill="#abd036"/>
    <path d="M10 160 H280 L270 176 H20 Z" fill="#d6d6d6"/>
  </svg>
  <div class="features">
    <div class="feature"><div class="feature-icon"><svg width="20" height="20" viewBox="0 0 20 20"><rect x="2" y="8" width="16" height="10" fill="none" stroke="#fff" stroke-width="2"/><path d="M1 8 L10 2 L19 8" fill="none" stroke="#fff" stroke-width="2"/></svg></div><div><h3>salons</h3><p>Lorem ipsum dolor sit amet,<br>consectetur adipiscing</p></div></div>
    <div class="feature"><div class="feature-icon"><svg width="20" height="20" viewBox="0 0 20 20"><rect x="3" y="4" width="14" height="14" fill="none" stroke="#fff" stroke-width="2"/><path d="M3 9 H17" stroke="#fff" stroke-width="2"/></svg></div><div><h3>agreements</h3><p>Lorem ipsum dolor sit amet,<br>consectetur adipiscing</p></div></div>
    <div class="feature"><div class="feature-icon"><svg width="20" height="20" viewBox="0 0 20 20"><path d="M3 17 V11 M8 17 V7 M13 17 V9 M18 17 V3" stroke="#fff" stroke-width="3"/></svg></div><div><h3>Treatments for booking</h3><p>Lorem ipsum dolor sit amet,<br>consectetur adipiscing</p></div></div>
    <div class="feature"><div class="feature-icon"><svg width="20" height="20" viewBox="0 0 20 20"><path d="M4 16 L16 4 M4 4 L16 16" stroke="#fff" stroke-width="2"/><circle cx="4" cy="16" r="2.5" fill="#fff"/><circle cx="16" cy="16" r="2.5" fill="#fff"/></svg></div><div><h3>Hairdressers booking</h3><p>Lorem ipsum dolor sit amet,<br>consectetur adipiscing</p></div></div>
    <div class="feature"><div class="feature-icon"><svg width="20" height="20" viewBox="0 0 20 20"><circle cx="10" cy="10" r="7" fill="none" stroke="#fff" stroke-width="2"/><path d="M6 10 L9 13 L14 7" fill="none" stroke="#fff" stroke-width="2"/></svg></div><div><h3>Reliable reviews</h3><p>Lorem ipsum dolor sit amet,<br>consectetur adipiscing</p></div></div>
  </div>
</section>

<section class="app">
  <div class="app-photo" role="img" aria-label="Green-tinted photo of a barber shop interior"></div>
  <svg class="notch-top" width="80" height="34" viewBox="0 0 80 34"><path d="M0 0 H80 L40 34 Z" fill="#fff"/></svg>
  <div class="phones" role="img" aria-label="Illustration of two smartphones showing the TrimTable app"></div>
  <svg class="phones" viewBox="0 0 260 310" aria-hidden="true">
    <rect x="0" y="40" width="130" height="250" rx="16" fill="#f2f2f2"/>
    <rect x="10" y="70" width="110" height="190" fill="#abd036"/>
    <rect x="100" y="0" width="150" height="300" rx="18" fill="#1e1e1e"/>
    <rect x="110" y="36" width="130" height="228" fill="#eaeaea"/>
    <rect x="110" y="36" width="130" height="40" fill="#abd036"/>
  </svg>
  <div class="app-copy">
    <h2 class="cond">ALL THE HAIRDRESSERS</h2>
    <p class="lead">of Netherlands in your pocket!</p>
    <p class="small">Download the TrimTable APP and always find a salon to make a quick booking on the go.</p>
    <div class="badges"><span class="badge"></span><span class="badge"></span></div>
    <span class="app-btn">DOWNLOAD OUR PHONE APP</span>
  </div>
</section>

<section class="steps">
  <svg class="notch-bottom" width="80" height="34" viewBox="0 0 80 34"><path d="M0 0 H80 L40 34 Z" fill="#a3c733"/></svg>
  <h2 class="cond">HOW DOES IT WORK?</h2>
  <svg class="steps-line" width="680" height="4"><line x1="0" y1="2" x2="680" y2="2" stroke="#c3c3c3" stroke-width="2" stroke-dasharray="6 6"/></svg>
  <div class="step" style="left:130px">
    <svg width="90" height="110" viewBox="0 0 90 110"><path d="M45 108 L20 70 A40 40 0 1 1 70 70 Z" fill="#abd036"/><circle cx="45" cy="42" r="32" fill="#fff"/><circle cx="42" cy="38" r="12" fill="none" stroke="#3f4548" stroke-width="4"/><path d="M51 47 L62 58" stroke="#3f4548" stroke-width="5"/></svg>
    <h3>Search &amp; Find hairdresser</h3>
    <p>Lorem ipsum dolor sit amet, consectetur adipiscing elit, sed do eiusmod tempor.</p>
  </div>
  <div class="step" style="left:470px">
    <svg width="90" height="110" viewBox="0 0 90 110"><path d="M45 108 L20 70 A40 40 0 1 1 70 70 Z" fill="#abd036"/><circle cx="45" cy="42" r="32" fill="#fff"/><rect x="29" y="30" width="32" height="20" fill="none" stroke="#3f4548" stroke-width="3"/><path d="M24 55 H66" stroke="#3f4548" stroke-width="4"/></svg>
    <h3>Book your appointment<br>online with 100% certainty</h3>
    <p>Lorem ipsum dolor sit amet, consectetur adipiscing elit, sed do eiusmod.</p>
  </div>
  <div class="step" style="left:810px">
    <svg width="90" height="110" viewBox="0 0 90 110"><path d="M45 108 L20 70 A40 40 0 1 1 70 70 Z" fill="#abd036"/><circle cx="45" cy="42" r="32" fill="#fff"/><circle cx="45" cy="42" r="16" fill="none" stroke="#3f4548" stroke-width="3"/><circle cx="39" cy="38" r="2" fill="#3f4548"/><circle cx="51" cy="38" r="2" fill="#3f4548"/><path d="M38 46 Q45 53 52 46" fill="none" stroke="#3f4548" stroke-width="3"/></svg>
    <h3>Enjoy your new hairstyle</h3>
    <p>Lorem ipsum dolor sit amet, consectetur adipiscing elit, sed do eiusmod tempor.</p>
  </div>
</section>

<section class="news">
  <div class="news-photo" role="img" aria-label="Dark photo of hands holding a smartphone"></div>
  <div class="news-shade"></div>
  <h2 class="cond">NICE TRIMTABLE GET TIPS?</h2>
  <p class="lead">Subscribe to our newsletter to be notified<br>about new salon releases</p>
  <div class="news-form">
    <div class="news-input"><svg width="24" height="18" viewBox="0 0 24 18"><rect x="1" y="1" width="22" height="16" fill="none" stroke="#777" stroke-width="2"/><path d="M1 1 L12 10 L23 1" fill="none" stroke="#777" stroke-width="2"/></svg>Your email address</div>
    <div class="news-btn">SIGN UP</div>
  </div>
</section>

<footer class="footer">
  <div class="foot-logo"><span class="mark"></span><span>TrimTable</span></div>
  <div class="foot-col" style="left:260px"><h4>QUICK LINKS</h4><ul><li>Salons Amsterdam</li><li>Salons Rotterdam</li><li>Salons Utrecht</li><li>Salons Leiden</li><li>Salons Eindhoven</li></ul></div>
  <div class="foot-col" style="left:460px"><h4>TRIMTABLE</h4><ul><li>About us</li><li>Treatments for booking</li><li>Hairdressers booking</li><li>Reliable reviews</li></ul></div>
  <div class="foot-col social" style="left:680px"><h4>OFFERING</h4><ul><li><i></i>Friendwall</li><li><i></i>Chirpline</li><li><i></i>Worknet</li></ul></div>
  <div class="foot-col" style="left:880px"><h4>CONTACT US</h4><ul><li>TrimTable</li><li>1234 AB Amsterdam</li><li>&nbsp;</li><li>+31 (0)20 555 0147</li><li>info@trimtable.com</li></ul></div>
</footer>
<div class="copyright">Copyright 2015 © TrimTable</div>

</body>
</html>
```